Brindle Market is an online marketing platform.

A daily deals site for consumers a way to bring in new clients for clients and this is who the business cards are for. Industries - Food and Drink, Things To Do, Beauty and Spas, Staycations and Services.
Logo on one side.
Name - Owen Carradine
Job Title - Sales Director
Phone Number - 07912583046
Email - owen@brindlemarket.co.uk
need same for second person
Name - Tessa Lindqvist
Job Title - Operations Director
Phone Number - 01632884275
Email - tessa@brindlemarket.co.uk
Bottom Right - Facebook Icon, Insta Icon, Twitter Icon
Target Market(s)
Business owners of the above industries
Contact Information for Business Card
Name - Owen Carradine
Name - Tessa Lindqvist
Look and feel
Each slider illustrates characteristics of the customer's brand and the style your logo design should communicate.

```html
<!DOCTYPE html>
<html lang="en">
<head>
<meta charset="utf-8">
<title>Brindle Market – Business Cards</title>
<link rel="stylesheet" href="https://fonts.googleapis.com/css2?family=Lato:wght@300;400;700&display=swap">
<style>
  :root {
    --brand-blue: #0f5aa8;
    --ink-grey: #555a5f;
    --card-white: #ffffff;
    --backdrop: #3b3b3c;
    --social-mid: #4f8fd0;
  }
  * { margin: 0; padding: 0; box-sizing: border-box; }
  html, body {
    width: 1200px; height: 900px; overflow: hidden;
    background: var(--backdrop);
    font-family: "Lato", Arial, sans-serif;
  }
  .stage { position: relative; width: 1200px; height: 900px; }

  .card {
    position: absolute; width: 509px; height: 290px;
    background: var(--card-white);
  }
  .card--owen  { left: 63px;  top: 160px; }
  .card--tessa { left: 628px; top: 160px; }
  .card--back  { left: 353px; top: 519px; background: var(--brand-blue); }

  .wordmark {
    position: absolute; display: flex; align-items: center; gap: 8px;
    color: var(--brand-blue); font-weight: 700;
  }
  .card .wordmark { right: 24px; top: 38px; font-size: 26px; }
  .wordmark__dot {
    width: 34px; height: 34px; border-radius: 50%;
    background: var(--brand-blue); flex: none;
  }
  .card--back .wordmark {
    left: 0; right: 0; top: 118px; justify-content: center;
    color: var(--card-white); font-size: 40px; gap: 12px;
  }
  .card--back .wordmark__dot { width: 52px; height: 52px; background: var(--card-white); }

  .person { position: absolute; left: 30px; top: 150px; }
  .person__name { color: var(--brand-blue); font-weight: 700; font-size: 18px; line-height: 1; }
  .person__role { color: var(--ink-grey); font-weight: 300; font-size: 12px; margin-top: 8px; }

  .rule {
    position: absolute; left: 30px; right: 24px; top: 202px;
    height: 1.5px; background: var(--brand-blue);
  }

  .contacts { position: absolute; left: 30px; top: 211px; list-style: none; }
  .contacts li {
    display: flex; align-items: center; gap: 8px;
    color: var(--ink-grey); font-size: 12px; height: 20px;
  }
  .contacts svg { width: 10px; height: 10px; fill: var(--brand-blue); flex: none; }

  .socials { position: absolute; right: 24px; top: 248px; display: flex; gap: 6px; }
  .socials span { width: 17px; height: 17px; border-radius: 50%; background: var(--brand-blue); }
  .socials span:nth-child(2) { background: var(--ink-grey); }
  .socials span:nth-child(3) { background: var(--social-mid); }
</style>
</head>
<body>
<main class="stage">

  <section class="card card--owen">
    <div class="wordmark"><span class="wordmark__dot"></span>Brindle Market</div>
    <div class="person">
      <p class="person__name">Owen Carradine</p>
      <p class="person__role">Sales Director</p>
    </div>
    <div class="rule"></div>
    <ul class="contacts">
      <li><svg viewBox="0 0 10 10"><path d="M2 0.5 L3.6 2.6 L2.8 3.6 Q4 6 6.4 7.2 L7.4 6.4 L9.5 8 L8.4 9.5 Q1.5 8.5 0.5 1.6 Z"/></svg>07912583046</li>
      <li><svg viewBox="0 0 10 10"><path d="M0.5 2 H9.5 V8.5 H0.5 Z M1.2 2.6 L5 5.6 L8.8 2.6 V3.5 L5 6.5 L1.2 3.5 Z" fill-rule="evenodd"/></svg>owen@brindlemarket.co.uk</li>
      <li><svg viewBox="0 0 10 10"><circle cx="5" cy="5" r="4.5"/></svg>www.brindlemarket.co.uk</li>
    </ul>
    <div class="socials" aria-label="Social media"><span></span><span></span><span></span></div>
  </section>

  <section class="card card--tessa">
    <div class="wordmark"><span class="wordmark__dot"></span>Brindle Market</div>
    <div class="person">
      <p class="person__name">Tessa Lindqvist</p>
      <p class="person__role">Operations Director</p>
    </div>
    <div class="rule"></div>
    <ul class="contacts">
      <li><svg viewBox="0 0 10 10"><path d="M2 0.5 L3.6 2.6 L2.8 3.6 Q4 6 6.4 7.2 L7.4 6.4 L9.5 8 L8.4 9.5 Q1.5 8.5 0.5 1.6 Z"/></svg>01632884275</li>
      <li><svg viewBox="0 0 10 10"><path d="M0.5 2 H9.5 V8.5 H0.5 Z M1.2 2.6 L5 5.6 L8.8 2.6 V3.5 L5 6.5 L1.2 3.5 Z" fill-rule="evenodd"/></svg>tessa@brindlemarket.co.uk</li>
      <li><svg viewBox="0 0 10 10"><circle cx="5" cy="5" r="4.5"/></svg>www.brindlemarket.co.uk</li>
    </ul>
    <div class="socials" aria-label="Social media"><span></span><span></span><span></span></div>
  </section>

  <section class="card card--back">
    <div class="wordmark"><span class="wordmark__dot"></span>Brindle Market</div>
  </section>

</main>
</body>
</html>
```